Harborline Energy - needs a business card

Harborline Energy is a U.S. based diesel sourcing and distribution company that supports American oil & gas fields through providing quality product and consistent services.

Target Market(s)

Oil and Gas

Contact Information for Business Card

The background of the card must be white to ensure the logo pops.

Font styles to use
Serif
Sans Serif

Colors

Designer to choose colors to be used in the design.

Requirements
Must have
• Front of Card: Tag line: Harborline Energy, Powering America's Oil & Gas fields.
• Not sure if you guys do this part but just in case...
• Dale Menschow
• Owner/CEO
• C:555.318.4076
• E:Dmenschow@harborlineenergy.example
• W:Harborlineenergy.example
• Locations: Servicing the Powder River, DJ basin and Bakken formations.
• Back of Card: " Frac fueling is what we do. We understand how important diesel fuel is to your operation, which is why our main service line is Frac fueling. We assure our supply and stand by our service"

```html
<!DOCTYPE html>
<html lang="en">
<head>
<meta charset="utf-8">
<title>Harborline Energy – Business Card</title>
<link rel="stylesheet" href="https://fonts.googleapis.com/css2?family=Open+Sans:ital,wght@0,300;0,400;0,600;0,800;1,400&family=Noto+Serif:ital@1&display=swap">
<style>
  :root {
    --navy: #2b3a6b;
    --red: #d6333c;
    --grey: #7b7f88;
    --paper: #ffffff;
    --stage: #ecebe8;
    --faint: #f1f1f2;
  }
  * { box-sizing: border-box; margin: 0; padding: 0; }
  html, body { width: 1200px; height: 942px; overflow: hidden; }
  body {
    background: var(--stage);
    font-family: "Open Sans", sans-serif;
    color: var(--navy);
    display: flex;
    flex-direction: column;
    align-items: center;
    justify-content: center;
    gap: 50px;
  }
  .card {
    position: relative;
    width: 700px;
    height: 400px;
    background: var(--paper);
    border-radius: 26px;
    box-shadow: 0 6px 18px rgba(0,0,0,.12);
    overflow: hidden;
  }
  .rule { display: block; width: 40px; height: 3px; background: var(--red); }

  /* front */
  .front .identity { position: absolute; left: 56px; top: 40px; }
  .name { font-weight: 300; font-size: 30px; letter-spacing: 1px; text-transform: uppercase; }
  .role { font-family: "Noto Serif", serif; font-style: italic; font-size: 17px; color: var(--grey); margin-top: 2px; }
  .front .rule.r1 { position: absolute; left: 190px; top: 124px; }
  .contacts { position: absolute; left: 80px; top: 142px; list-style: none; font-size: 18px; line-height: 30px; }
  .contacts li { display: flex; align-items: center; gap: 10px; }
  .contacts svg { width: 14px; height: 14px; flex: none; }
  .front .rule.r2 { position: absolute; left: 56px; top: 244px; }
  .coverage { position: absolute; left: 56px; top: 260px; font-size: 18px; line-height: 26px; }
  .faint-mark { position: absolute; left: 300px; top: 300px; width: 240px; height: 240px; border-radius: 50%; background: var(--faint); }
  .front .brand { position: absolute; right: 44px; bottom: 28px; }

  .brand { display: flex; align-items: center; gap: 12px; white-space: nowrap; }
  .brand-dot { width: 34px; height: 34px; border-radius: 50%; background: var(--navy); flex: none; }
  .brand-name { font-weight: 800; font-size: 28px; letter-spacing: 1px; color: var(--navy); text-transform: uppercase; }

  /* back */
  .back .brand { position: absolute; left: 50%; top: 100px; transform: translateX(-50%); }
  .timeline { position: absolute; left: 48px; right: 48px; top: 200px; height: 2px; background: var(--navy); }
  .marker { position: absolute; top: 188px; width: 26px; height: 26px; }
  .point { position: absolute; top: 226px; font-size: 15px; line-height: 21px; text-align: center; }
  .point.accent { color: var(--red); width: 140px; }
  .point.main { color: var(--navy); width: 300px; left: 200px; }
  .p1 { left: 26px; }
  .p3 { right: 26px; }
  .m1 { left: 83px; } .m2 { left: 337px; } .m3 { left: 591px; }
</style>
</head>
<body>
  <section class="card front">
    <div class="faint-mark" role="img" aria-label="Faint brand emblem decoration"></div>
    <div class="identity">
      <h1 class="name">Dale Menschow</h1>
      <p class="role">Owner/CEO</p>
    </div>
    <span class="rule r1"></span>
    <ul class="contacts">
      <li><svg viewBox="0 0 14 14"><rect x="3" y="1" width="8" height="12" rx="1.5" fill="none" stroke="#d6333c" stroke-width="1.6"/></svg>555.318.4076</li>
      <li><svg viewBox="0 0 14 14"><rect x="1" y="3" width="12" height="8" fill="#d6333c"/><path d="M1 3l6 5 6-5" fill="none" stroke="#fff" stroke-width="1"/></svg>Dmenschow@harborlineenergy.example</li>
      <li><svg viewBox="0 0 14 14"><circle cx="7" cy="7" r="6" fill="#d6333c"/><path d="M1 7h12M7 1c-3 3-3 9 0 12M7 1c3 3 3 9 0 12" fill="none" stroke="#fff" stroke-width=".8"/></svg>Harborlineenergy.example</li>
    </ul>
    <span class="rule r2"></span>
    <p class="coverage">Servicing the<br>Powder River, DJ basin and Bakken formations</p>
    <div class="brand">
      <span class="brand-dot"></span>
      <span class="brand-name">Harborline Energy</span>
    </div>
  </section>

  <section class="card back">
    <div class="brand">
      <span class="brand-dot"></span>
      <span class="brand-name">Harborline Energy</span>
    </div>
    <div class="timeline"></div>
    <svg class="marker m1" viewBox="0 0 26 26"><path d="M13 2C13 2 4 12 4 17a9 9 0 0 0 18 0C22 12 13 2 13 2z" fill="#fff" stroke="#d6333c" stroke-width="2"/></svg>
    <svg class="marker m2" viewBox="0 0 26 26"><path d="M13 2C13 2 4 12 4 17a9 9 0 0 0 18 0C22 12 13 2 13 2z" fill="#fff" stroke="#d6333c" stroke-width="2"/></svg>
    <svg class="marker m3" viewBox="0 0 26 26"><path d="M13 2C13 2 4 12 4 17a9 9 0 0 0 18 0C22 12 13 2 13 2z" fill="#fff" stroke="#d6333c" stroke-width="2"/></svg>
    <p class="point accent p1">Frac fueling is<br>what we do</p>
    <p class="point main">We understand how important diesel fuel is to your operation, which is why our main service line is Frac fueling</p>
    <p class="point accent p3">We assure our supply and stand by our service</p>
  </section>
</body>
</html>
```